BOLD & MINIMALIST DESIGN NEEDED

We want a very bold but minimalistic business card design that is impactful and utilizes both sides of the business card. Our current logo is included for your use.

We want bold fonts and good use of negative space. We don't want the logo to overpower the design.

Target Market(s)

Professionals who are building new commercial buildings.

Industry/Entity Type

Construction

Contact Information for Business Card

Name, Title, email, office phone, cell phone, website

Font styles to use
Serif
Sans Serif

Requirements
Must have
• Bold design!

```html
<!DOCTYPE html>
<html lang="en">
<head>
<meta charset="utf-8">
<title>Ridgeline Design + Build — Business Card</title>
<link href="https://fonts.googleapis.com/css2?family=Poppins:wght@400;500;800&display=swap" rel="stylesheet">
<style>
  :root {
    --ink: #0b0b0c;
    --green: #82c341;
    --paper: #ffffff;
    --backdrop: #1c1c1e;
  }
  * { margin: 0; padding: 0; box-sizing: border-box; }
  html, body {
    width: 1200px; height: 1200px; overflow: hidden;
    background: var(--backdrop);
    font-family: "Poppins", sans-serif;
    color: var(--ink);
  }
  .sheet {
    position: relative; width: 1200px; height: 1200px;
    display: flex; flex-direction: column; align-items: center; justify-content: center; gap: 60px;
  }
  .card {
    position: relative; width: 880px; height: 500px;
    background: var(--paper); overflow: hidden;
  }
  .band {
    position: absolute; left: 0; right: 0;
    background: var(--green);
    display: flex; align-items: center; justify-content: center;
  }

  /* Front side */
  .front .brand {
    position: absolute; top: 170px; left: 0; right: 0;
    display: flex; align-items: center; justify-content: center; gap: 18px;
  }
  .brand-mark { width: 30px; height: 30px; background: var(--green); }
  .brand-name {
    font-weight: 800; font-size: 40px; letter-spacing: 0.02em;
    color: var(--ink); white-space: nowrap;
  }
  .front .band { top: 340px; height: 74px; }
  .front .web {
    font-weight: 500; font-size: 22px; letter-spacing: 0.38em; color: var(--ink);
  }

  /* Back side */
  .back .wordmark {
    position: absolute; top: 52px; left: 0; right: 0;
    text-align: center; font-weight: 800; color: var(--ink); line-height: 1;
  }
  .wordmark .main { display: block; font-size: 96px; letter-spacing: 0.01em; }
  .wordmark .sub { display: block; font-size: 30px; letter-spacing: 0.42em; margin-top: 10px; padding-left: 0.42em; }

  .person {
    position: absolute; top: 270px; left: 90px; width: 270px; text-align: right;
  }
  .person-name { font-weight: 800; font-size: 32px; line-height: 1.1; }
  .person-title { font-weight: 400; font-size: 19px; letter-spacing: 0.14em; color: var(--green); }

  .divider {
    position: absolute; top: 262px; left: 386px; width: 3px; height: 104px; background: var(--green);
  }
  .contacts {
    position: absolute; top: 262px; left: 412px; list-style: none;
  }
  .contacts li {
    display: flex; align-items: center; gap: 14px;
    font-size: 21px; font-weight: 500; height: 35px;
  }
  .icon { width: 24px; height: 24px; flex: none; }

  .back .band { top: 392px; height: 62px; }
  .address { font-weight: 500; font-size: 24px; color: var(--ink); }
</style>
</head>
<body>
<main class="sheet">

  <section class="card front" aria-label="Card front">
    <div class="brand">
      <span class="brand-mark"></span>
      <span class="brand-name">RIDGELINE DESIGN + BUILD</span>
    </div>
    <div class="band">
      <span class="web">www.ridgelinebuild.com</span>
    </div>
  </section>

  <section class="card back" aria-label="Card back">
    <h1 class="wordmark">
      <span class="main">RIDGELINE</span>
      <span class="sub">DESIGN + BUILD</span>
    </h1>

    <div class="person">
      <p class="person-name">OWEN MARSH</p>
      <p class="person-title">MANAGER</p>
    </div>

    <div class="divider"></div>

    <ul class="contacts">
      <li>
        <svg class="icon" viewBox="0 0 24 24" aria-hidden="true">
          <circle cx="12" cy="12" r="12" fill="#82c341"/>
          <path d="M8.2 6.5l2 2.2-1 1.4c.7 1.6 1.9 2.9 3.6 3.7l1.4-1 2.2 2-1.2 1.8c-3.9-.4-7.4-3.9-8-8z" fill="#fff"/>
        </svg>
        (555) 010-2040
      </li>
      <li>
        <svg class="icon" viewBox="0 0 24 24" aria-hidden="true">
          <circle cx="12" cy="12" r="12" fill="#82c341"/>
          <rect x="6" y="8" width="12" height="8.5" fill="none" stroke="#fff" stroke-width="1.4"/>
          <path d="M6 8l6 5 6-5" fill="none" stroke="#fff" stroke-width="1.4"/>
        </svg>
        info@ridgelinebuild.com
      </li>
      <li>
        <svg class="icon" viewBox="0 0 24 24" aria-hidden="true">
          <circle cx="12" cy="12" r="12" fill="#82c341"/>
          <circle cx="12" cy="12" r="6" fill="none" stroke="#fff" stroke-width="1.3"/>
          <ellipse cx="12" cy="12" rx="2.6" ry="6" fill="none" stroke="#fff" stroke-width="1.2"/>
          <path d="M6 12h12" stroke="#fff" stroke-width="1.2"/>
        </svg>
        www.ridgelinebuild.com
      </li>
    </ul>

    <div class="band">
      <span class="address">PO Box 48, 2nd Street, Harbor City</span>
    </div>
  </section>

</main>
</body>
</html>
```